Australian Trucking Company Requires Professional Looking Stationary

We require a professional looking stationary design that incorporates our newly designed logo.

Our business, called "Vell Haulage Contracting", provides contracting work, transport and logistics to business in Western Australia particularly with links to the mining sector.

We are a small business looking to expand and our new logo and our new stationary will help develop our brand image in our market place.

Target Market(s)

Businesses and Corporation with links to the Mining Sector

Industry/Entity Type

Small Business

Requirements
Must have
• The letterhead must have the following details:
The new logo

Text saying: "Vell Haulage Pty Ltd (ACN 582 306 917) ATF The Vell Discretionary Trust T/AS"
"ABN 71 840 239 568"
Address "P.O Box 817 Ashbury WA, 6912"
Phone: 08 9172 5840
Email: vellhaul@mailnest.com.au

The text on the letterhead should be editable as the details are likely to change in the near future. Provision should be made for a website address all though one isn't available at the moment.

The styling, layout and font text is entirely up to the designer.

```html
<!DOCTYPE html>
<html lang="en">
<head>
<meta charset="utf-8">
<title>Vell Haulage Contracting — Envelope</title>
<link rel="stylesheet" href="https://fonts.googleapis.com/css2?family=Titillium+Web:wght@400;700&display=swap">
<style>
  :root {
    --backdrop: #e6e4e0;
    --paper: #ffffff;
    --brand-red: #b3161c;
    --ink: #3a3a3a;
    --mark-grey: #8a8a8a;
  }
  * { margin: 0; padding: 0; box-sizing: border-box; }
  html, body {
    width: 1200px;
    height: 720px;
    overflow: hidden;
    background: var(--backdrop);
  }
  body {
    display: flex;
    align-items: center;
    justify-content: center;
    font-family: "Titillium Web", sans-serif;
  }
  .envelope {
    position: relative;
    width: 1000px;
    height: 500px;
    background: var(--paper);
    box-shadow: 0 2px 6px rgba(0,0,0,0.12);
  }
  .sender {
    position: absolute;
    top: 42px;
    left: 48px;
  }
  .brand {
    display: flex;
    align-items: center;
    gap: 14px;
    margin-bottom: 14px;
  }
  .brand-mark {
    width: 54px;
    height: 54px;
    border-radius: 50%;
    background: var(--mark-grey);
  }
  .brand-name {
    font-weight: 700;
    font-size: 21px;
    line-height: 1;
    letter-spacing: 0.04em;
    text-transform: uppercase;
    color: var(--brand-red);
  }
  .brand-name span { display: block; }
  .sender-details {
    font-style: normal;
    font-weight: 400;
    font-size: 12.5px;
    line-height: 1.35;
    color: var(--ink);
  }
  .sender-details p { white-space: nowrap; }
  .base-rule {
    position: absolute;
    left: 0;
    right: 0;
    bottom: 26px;
    height: 4px;
    background: var(--brand-red);
  }
</style>
</head>
<body>
  <main class="envelope">
    <section class="sender">
      <div class="brand">
        <div class="brand-mark" aria-hidden="true"></div>
        <div class="brand-name">
          <span>Vell</span>
          <span>Haulage</span>
          <span>Contracting</span>
        </div>
      </div>
      <address class="sender-details">
        <p>P.O Box 817 Ashbury WA, 6912</p>
        <p>Vell Haulage Pty Ltd (ACN 582 306 917)</p>
        <p>ATF The Vell Discretionary Trust T/AS</p>
        <p>ABN 71 840 239 568</p>
      </address>
    </section>
    <div class="base-rule" aria-hidden="true"></div>
  </main>
</body>
</html>
```